Stationery and Logo Design Project for new NZ Accounting Firm

Our company name is based in Auckland, New Zealand and is called DHW CA Limited. We are a chartered accountancy firm hence the CA abbreviations.

We need a full logo stationery design: Logo, Letterhead, Business Card and Compliments slip.

We are looking for a bold, modern and clean/simple design that makes us stand out. We want to stand out as professionals in the industry and would like the logo and stationery that our clients see to convey this image. We also want to break away from the traditional boring views of book/bean accountants. We are not doing the same old things others are doing and are mainly cloud based but with face to face business relationship focused as well.

We see ourselves as business advisers that provide more than just filing their tax returns. We want to add value to their business and be a partner in their business ventures.

We want the logo to convey the above and also attract potential clients when they see our ads among the thousands on vornix and the civic atlas.

The logo can be for the "DHW" with CA Ltd seperately or a logo/design beside the DHW. But open to other suggestions or concept.

Hi Designers

The designs I have received so far is not quite what I want.

I want something modern and bold that is DIFFERENT from others, from the usual logo designs. Some logo that when people look at it they will remember it as opposed to fading in the background of other competitors' logo.

Lower case lettering for the DHW could be something to explore as I have not seen a lot of these and they do appeal to me.

Thanks

We can focus on the logo first as that will form the main part for all stationery.

Reason: Final stages of choosing a logo design so need to time for designers to submit the letterhead, namecards designs.

Our target clients are small to medium business ranging from the sole trader to 50 employees businesses

Business

```html
<!DOCTYPE html>
<html lang="en">
<head>
<meta charset="utf-8">
<title>DHW CA Limited – Business Card</title>
<link href="https://fonts.googleapis.com/css2?family=PT+Sans:wght@400;700&display=swap" rel="stylesheet">
<style>
  :root {
    --backdrop: #d9d9d9;
    --card-white: #ffffff;
    --card-shade: #ececec;
    --card-black: #0a0a0a;
    --card-black-glow: #2a2a2a;
    --navy: #1b3d7a;
    --navy-deep: #14285a;
    --slate: #5a5a5a;
    --ink: #1e1e1e;
    --rule: #2b2b2b;
    --white: #ffffff;
    --icon-bg: #e4e8f0;
  }
  * { margin: 0; padding: 0; box-sizing: border-box; }
  html, body { width: 1200px; height: 900px; overflow: hidden; }
  body {
    background: var(--backdrop);
    font-family: "PT Sans", Arial, sans-serif;
    position: relative;
  }
  .card {
    position: absolute;
    width: 540px;
    height: 309px;
    border-radius: 2px;
    box-shadow: 0 8px 24px rgba(0,0,0,0.25);
    overflow: hidden;
  }

  /* Card back */
  .card-back {
    left: 40px; top: 70px;
    background: radial-gradient(circle at 50% 50%, var(--card-black-glow) 0%, var(--card-black) 62%);
    color: var(--white);
  }
  .card-back .brand-name {
    position: absolute; left: 0; right: 0; top: 104px;
    text-align: center;
    font-family: "PT Sans", Arial, sans-serif;
    font-weight: 400;
    font-size: 40px;
    letter-spacing: 2px;
    color: var(--white);
  }
  .card-back .web {
    position: absolute; left: 0; right: 0; top: 206px;
    text-align: center;
    font-size: 14px; letter-spacing: 4px;
    color: var(--white);
  }

  /* Card front */
  .card-front {
    left: 620px; top: 70px;
    background: linear-gradient(160deg, var(--card-white) 30%, var(--card-shade) 100%);
    color: var(--ink);
  }
  .card-front .brand-name {
    position: absolute; left: 34px; top: 34px;
    font-family: "PT Sans", Arial, sans-serif;
    font-weight: 400;
    font-size: 30px;
    letter-spacing: 1px;
    color: var(--slate);
  }
  .card-front .person {
    position: absolute; right: 34px; top: 118px;
    text-align: right;
  }
  .person-name { font-weight: 700; font-size: 18px; color: var(--navy-deep); }
  .person-role { font-size: 15px; color: var(--ink); }
  .card-front .rule {
    position: absolute; left: 34px; right: 34px; top: 166px;
    height: 1px; background: var(--rule);
  }
  .card-front .address {
    position: absolute; left: 34px; top: 180px;
    font-size: 14px; color: var(--ink);
  }
  .contacts {
    position: absolute; left: 34px; top: 208px;
    display: grid; grid-template-columns: 170px 220px; row-gap: 8px;
    font-size: 14px; color: var(--ink);
  }
  .contact { display: flex; align-items: center; gap: 8px; }
  .contact svg { width: 16px; height: 16px; flex: none; }
  .card-front .band-line {
    position: absolute; left: 0; right: 0; bottom: 20px;
    height: 3px; background: linear-gradient(90deg, var(--navy-deep), var(--navy), #7fa0d8);
  }
  .card-front .band {
    position: absolute; left: 0; right: 0; bottom: 0;
    height: 20px; background: linear-gradient(90deg, #000, #2a2a2a 70%, #000);
  }

  /* Name panel */
  .name-panel {
    position: absolute; left: 40px; top: 560px;
    width: 400px; height: 240px;
    background: var(--white);
    box-shadow: 0 4px 14px rgba(0,0,0,0.15);
    display: flex; align-items: center; justify-content: center;
  }
  .name-panel .brand-name {
    font-family: "PT Sans", Arial, sans-serif;
    font-weight: 400; font-size: 40px; letter-spacing: 1px;
    color: var(--navy);
  }
</style>
</head>
<body>

  <section class="card card-back">
    <div class="brand-name">DHW CA Limited</div>
    <div class="web">www.dhwca.co.nz</div>
  </section>

  <section class="card card-front">
    <div class="brand-name">DHW CA Limited</div>
    <div class="person">
      <div class="person-name">Mara Ellison</div>
      <div class="person-role">Chartered Accountant</div>
    </div>
    <div class="rule"></div>
    <div class="address">14 Harbour Lane, Ponsonby, PO Box 3172</div>
    <div class="contacts">
      <div class="contact">
        <svg viewBox="0 0 16 16" aria-hidden="true"><rect width="16" height="16" rx="2" fill="#e4e8f0"/><path d="M3 6c0-2 10-2 10 0v1h-3V6H6v1H3z M4 8h8l1 4H3z" fill="#1b3d7a"/></svg>
        <span>(09) 376 2408</span>
      </div>
      <div class="contact">
        <svg viewBox="0 0 16 16" aria-hidden="true"><rect width="16" height="16" rx="2" fill="#e4e8f0"/><text x="8" y="12" font-size="11" font-weight="700" text-anchor="middle" fill="#1b3d7a" font-family="Arial, sans-serif">@</text></svg>
        <span>info@dhwca.co.nz</span>
      </div>
      <div class="contact">
        <svg viewBox="0 0 16 16" aria-hidden="true"><rect width="16" height="16" rx="2" fill="#e4e8f0"/><rect x="5" y="3" width="6" height="4" fill="none" stroke="#1b3d7a"/><rect x="3" y="7" width="10" height="4" rx="1" fill="#1b3d7a"/><rect x="5" y="10" width="6" height="3" fill="#fff" stroke="#1b3d7a"/></svg>
        <span>(09) 376 2409</span>
      </div>
      <div class="contact">
        <svg viewBox="0 0 16 16" aria-hidden="true"><rect width="16" height="16" rx="2" fill="#e4e8f0"/><circle cx="8" cy="8" r="5" fill="none" stroke="#1b3d7a" stroke-width="1.3"/><ellipse cx="8" cy="8" rx="2" ry="5" fill="none" stroke="#1b3d7a"/><line x1="3" y1="8" x2="13" y2="8" stroke="#1b3d7a"/></svg>
        <span>www.dhwca.co.nz</span>
      </div>
    </div>
    <div class="band-line"></div>
    <div class="band"></div>
  </section>

  <section class="name-panel">
    <span class="brand-name">DHW CA Limited</span>
  </section>

</body>
</html>
```